Hotel Newsletter Design

We need 4 newsletter templates for a luxurious hotel. The templates only differ in the headers (basically each has different images based on a certain theme and/or distinguishing colours). Please feel free to use other colour that those on the webpage of the hotel.

Previous newsletters were these:

"Wine bar" - http://www.palemoorinn.example/newsletter.php?id=76&lang=en
"Feast" - http://www.palemoorinn.example/newsletter.php?id=75&lang=en
"Hotel" - http://www.palemoorinn.example/newsletter.php?id=77&lang=en
"Restaurant" - http://www.palemoorinn.example/newsletter.php?id=78&lang=en

These were too basic and old-fashioned, we need something more UP-TO-DATE, FRESH, MORE MODERN DESIGN.

The final newsletter will be an HTML page with an editable section.

So upon designing please pay attention to leave a space for editable content, which is going to be text and images.

Header and footer required, these won't be editable.

The 4 different header themes are Wine bar, Hotel, Feast, Restaurant.

the website of the hotel:
http://www.palemoorinn.example/
images that can be used:
http://www.vrelkopix.example/temp/brana/images.zip

Target Market(s)

Luxurious Hotel Visitors

Industry/Entity Type

Hospitality

Requirements
Must have
• Logo in the header, address and contact in the footer
Nice to have
• Modern design
Should not have
• Old fashioned design

```html
<!DOCTYPE html>
<html lang="en">
<head>
<meta charset="utf-8">
<title>Pale Moor Inn — Wine Bar Newsletter</title>
<link rel="stylesheet" href="https://fonts.googleapis.com/css2?family=Noto+Sans:wght@400;700&family=Roboto:wght@100;300&family=Cormorant+Garamond:wght@600&display=swap">
<style>
  :root {
    --page-plum: #4b0d40;
    --page-plum-dark: #3a0832;
    --card-edge: #e4e4e4;
    --card-mid: #fbfbfb;
    --accent-red: #b3121c;
    --heading-grey: #8a8a8a;
    --body-grey: #b9b9b9;
    --strong-grey: #a9a9a9;
    --footer-maroon: #5c0a1e;
    --footer-maroon-dark: #3f0514;
    --white: #ffffff;
    --body-font: "Noto Sans", Arial, sans-serif;
    --heading-font: "Roboto", Arial, sans-serif;
  }
  * { margin: 0; padding: 0; box-sizing: border-box; }
  html, body {
    width: 1200px; height: 2400px; overflow: hidden;
    background: radial-gradient(ellipse at 50% 40%, var(--page-plum) 0%, var(--page-plum-dark) 100%);
  }
  .newsletter {
    position: absolute; left: 216px; top: 16px; width: 803px; height: 2336px;
    background: linear-gradient(90deg, var(--card-edge) 0%, var(--card-mid) 18%, var(--card-mid) 82%, var(--card-edge) 100%);
    box-shadow: 0 0 10px rgba(0,0,0,0.6);
    overflow: hidden;
  }
  .header {
    position: absolute; left: 0; top: 0; width: 803px; height: 597px; overflow: hidden;
  }
  .header-visual {
    position: absolute; inset: 0;
    background:
      linear-gradient(180deg, rgba(110,8,10,0.85) 0%, rgba(0,0,0,0) 35%),
      linear-gradient(90deg, #8c1a12 0%, #c0391a 30%, #d8862a 55%, #c9a530 75%, #d8337a 100%);
  }
  .logo-box {
    position: absolute; left: 266px; top: 26px; width: 249px; height: 248px;
    background: var(--white);
    box-shadow: 3px 3px 6px rgba(0,0,0,0.45);
    display: flex; flex-direction: column; align-items: center; justify-content: center; gap: 18px;
  }
  .logo-mark { width: 64px; height: 64px; border-radius: 50%; background: var(--accent-red); }
  .logo-name {
    font-family: "Cormorant Garamond", Georgia, serif; font-weight: 600;
    font-size: 21px; letter-spacing: 1px; color: var(--accent-red);
  }
  .header-theme {
    position: absolute; left: 144px; top: 486px;
    font-family: var(--heading-font); font-weight: 100;
    font-size: 130px; line-height: 1; letter-spacing: 4px; color: var(--white);
    white-space: nowrap;
  }
  .story-photo {
    position: absolute; border: 3px solid var(--white);
    box-shadow: 0 0 3px rgba(0,0,0,0.3);
  }
  .story-heading {
    position: absolute; font-family: var(--heading-font); font-weight: 300;
    font-size: 26px; line-height: 1; color: var(--heading-grey); white-space: nowrap;
  }
  .story-heading .lead { color: var(--accent-red); }
  .story-icon { position: absolute; width: 19px; height: 19px; }
  .story-text {
    position: absolute; left: 558px; width: 339px;
    font-family: var(--body-font); font-size: 14.4px; line-height: 21.2px;
    color: var(--body-grey); text-align: justify;
  }
  .story-text { left: 342px; }
  .story-text p + p { margin-top: 21.2px; }
  .story-text strong { color: var(--strong-grey); font-weight: 700; }
  .story-text .menu-link { color: var(--accent-red); font-weight: 700; text-decoration: none; }
  .news-block {
    position: absolute; left: 32px; top: 2130px; width: 690px;
    font-family: var(--body-font); font-size: 14.4px; line-height: 25px; color: var(--body-grey);
  }
  .news-block h3 { font-size: 14.4px; font-weight: 700; color: var(--strong-grey); }
  .footer {
    position: absolute; left: 5px; top: 2275px; width: 794px; height: 58px;
    background: linear-gradient(180deg, var(--footer-maroon) 0%, var(--footer-maroon-dark) 100%);
  }
  .footer-contact {
    position: absolute; left: 12px; top: 7px;
    font-family: var(--body-font); font-weight: 700; font-size: 11px; line-height: 14.5px; color: var(--white);
  }
  .footer-partner {
    position: absolute; right: 32px; top: 13px; display: flex; align-items: center; gap: 10px;
    font-family: var(--body-font); font-weight: 700; font-size: 17px; color: var(--white);
  }
  .footer-partner .dot { width: 30px; height: 30px; border-radius: 50%; background: var(--white); }
</style>
</head>
<body>
<main class="newsletter">
  <header class="header">
    <div class="header-visual" role="img" aria-label="Collage of warm wine bar interior photos with glasses, bottles and patterned upholstery"></div>
    <div class="logo-box">
      <div class="logo-mark"></div>
      <div class="logo-name">PALE MOOR INN</div>
    </div>
    <div class="header-theme">WINE BAR</div>
  </header>

  <section class="story">
    <div class="story-photo" role="img" aria-label="Red Christmas baubles hanging on a fir branch with soft lights" style="left:21px;top:694px;width:298px;height:333px;background:radial-gradient(circle at 40% 45%,#5a2a1a 0%,#2a1210 55%,#120606 100%);"></div>
    <h2 class="story-heading" style="left:342px;top:654px;"><span class="lead">SEASONS</span> GREETINGS</h2>
    <svg class="story-icon" style="left:659px;top:658px;" viewBox="0 0 2 2"><rect width="1" height="1" fill="#7fd6c4"/><rect x="1" width="1" height="1" fill="#d8f06a"/><rect y="1" width="1" height="1" fill="#b3121c"/><rect x="1" y="1" width="1" height="1" fill="#d8337a"/></svg>
    <div class="story-text" style="top:683px;">
      <p>We would like to give heartfelt thanks to all of our friends and partners for their enthusiasm and tremendous support during this past year. It has been a pleasure working with each and every one of you and it's because of you that we can safely say we are where we are today. On behalf of the whole team at the Pale Moor Inn, we wish you a Merry Christmas and truly prosperous New Year! May your holiday season be aglow with warmth and filled by those you care about.</p>
      <p><strong>We look forward to seeing all of you in 2010!</strong></p>
      <p><strong>Always at your service,<br>Adrian Vellmar</strong></p>
    </div>
  </section>

  <section class="story">
    <div class="story-photo" role="img" aria-label="Snowy medieval old town street at dusk with a church spire" style="left:27px;top:1165px;width:274px;height:408px;background:linear-gradient(180deg,#1c3a78 0%,#3b5590 40%,#b07a3a 75%,#e8d8b8 100%);"></div>
    <h2 class="story-heading" style="left:330px;top:1121px;"><span class="lead">WHITE DAYS</span> IN TALLINN</h2>
    <svg class="story-icon" style="left:659px;top:1125px;" viewBox="0 0 2 2"><rect width="1" height="1" fill="#7fd6c4"/><rect x="1" width="1" height="1" fill="#d8f06a"/><rect y="1" width="1" height="1" fill="#b3121c"/><rect x="1" y="1" width="1" height="1" fill="#d8337a"/></svg>
    <div class="story-text" style="top:1166px;">
      <p>The medieval Tallinn Old Town is a special place no matter what season you happen to be visiting, but it truly sparkles during the colder months. Snow covered cobblestone streets, the warm glow of shop windows and the bustling Christmas market make it a truly magical sight when the mercury drops to a few degrees below zero. If you happen to be planning your trip here during the winter season, we suggest you take advantage of our '<strong>White Days Package</strong>', which includes three luxurious nights at our hotel, airport or harbour pick-up and transfer, a 2,5-hour private tour of the city on any day of your choosing and a buffet breakfast, delightfully prepared by our fantastic team at the acclaimed Pale Moor Restaurant. You certainly won't regret a visit to this heritage-listed site and we're quite sure you won't be disappointed with the 'white days' or the 'white nights'.</p>
    </div>
  </section>

  <section class="story">
    <div class="story-photo" role="img" aria-label="Champagne flutes with sparkling wine against a dark background" style="left:21px;top:1672px;width:261px;height:418px;background:radial-gradient(ellipse at 45% 35%,#e8e2a8 0%,#8a8450 25%,#1a1a18 60%,#080808 100%);"></div>
    <h2 class="story-heading" style="left:330px;top:1628px;"><span class="lead">NEW</span> YEAR'S EVE</h2>
    <svg class="story-icon" style="left:637px;top:1632px;" viewBox="0 0 2 2"><rect width="1" height="1" fill="#7fd6c4"/><rect x="1" width="1" height="1" fill="#d8f06a"/><rect y="1" width="1" height="1" fill="#b3121c"/><rect x="1" y="1" width="1" height="1" fill="#d8337a"/></svg>
    <div class="story-text" style="top:1666px;">
      <p>What could be better than spending New Year's Eve in the intimate, history-filled ambience of the Pale Moor Inn. We dare to say "Nothing could be better".</p>
      <p>Our 'New Year's Eve Package' includes, three wonderful nights of accommodation, airport or harbour pick-up and transfer in our personal shuttle, a 2,5-hour private, guided tour of the Old Town, a scrumptious 7-course New Year's Eve dinner with corresponding wines and 4.5 hours of heavy pampering at the famous Velora Spa. For just a taste of what you can expect, please see our full New Year's Eve <a class="menu-link" href="#">menu.</a></p>
      <p>If you're going to ring in the New Year or say goodbye to the Old Year in Tallinn, our team of professionals will take care of all the arrangements for you. To turn your celebrations into a memory that will last a lifetime, The Pale Moor Inn is at your beckon call.</p>
    </div>
  </section>

  <section class="news-block">
    <h3>News from Silk Avenue</h3>
    <p>December is a month of celebrations. Christmas. New Year's Eve…<br>In addition to spending quality time with our loved ones, we all have also several festive events to attend. In order to help you look your best, Silk Avenue is delighted to provide you with the following special offers in December.</p>
  </section>

  <footer class="footer">
    <div class="footer-contact">
      The Pale Moor Inn, Lindenrow 18/Kelder 4, Tallinn 10140 Estonia<br>
      Tel: +372 600 1400 Fax: 600 1401<br>
      Email: info@palemoorinn.example
    </div>
    <div class="footer-partner"><span class="dot"></span>Stayline</div>
  </footer>
</main>
</body>
</html>
```